High end boutique food product label

We are looking for a label design to be used on our range of high end food products. We don't have a design or colour scheme in mind and are interested to see what ideas are submitted.
We would like it to feel sophisticated, chic, and eye-catching.
All of our products are handmade in Australia using Australian ingredients.
The graphics for the label will need to be scaleable to be fit a variety of labels from small squat jars with labels sized 3.5cm high and 7cm wide, to tall thin bottles with labels that are 14cm high and 4.5cm wide.
We would be interested in working with the winning designer to create these different sized labels.
The label submitted for this project should be 14cm high and 4.5cm wide, it should include our logo (file supplied in .jpeg and .ai), the product name 'Extra Virgin Olive Oil' and the size '250ml'.
This is just the front label on a bottle, we are not expecting a rear label to be created currently.
You are welcome to use any fonts you think will look good but the fonts used in our logo are Allaina Medium and Bebas Kai Regular.

```html
<!DOCTYPE html>
<html lang="en">
<head>
<meta charset="utf-8">
<title>Harlow Pantry – Extra Virgin Olive Oil Label</title>
<link rel="stylesheet" href="https://fonts.googleapis.com/css2?family=Playfair+Display:wght@700&family=Oswald:wght@500&display=swap">
<style>
  :root {
    --backdrop: #efefef;
    --label: #ffffff;
    --ink-brown: #3b2416;
    --sand: #b9a37c;
    --gold-light: #f3d77a;
    --gold-mid: #d6a834;
    --gold-deep: #a77a1a;
    --leaf-light: #dfe9cf;
    --leaf-mid: #a9c08a;
    --olive: #6f8f3a;
  }
  * { box-sizing: border-box; margin: 0; padding: 0; }
  html, body {
    width: 1200px;
    height: 1000px;
    overflow: hidden;
    background: var(--backdrop);
  }
  .canvas {
    position: relative;
    width: 1200px;
    height: 1000px;
  }
  .label {
    position: absolute;
    left: 458px;
    top: 59px;
    width: 283px;
    height: 882px;
    background: var(--label);
    border-radius: 141.5px 141.5px 0 0;
    overflow: hidden;
  }
  .brand {
    position: absolute;
    top: 168px;
    left: 0;
    width: 100%;
    text-align: center;
    font-family: "Playfair Display", Georgia, serif;
    font-weight: 700;
    font-size: 34px;
    line-height: 1.05;
    color: var(--ink-brown);
    letter-spacing: 0.5px;
  }
  .gold-wave {
    position: absolute;
    top: 276px;
    left: 0;
    width: 283px;
    height: 60px;
  }
  .product {
    position: absolute;
    top: 380px;
    left: 0;
    width: 100%;
    text-align: center;
  }
  .product-grade {
    font-family: "Oswald", "Arial Narrow", sans-serif;
    font-weight: 500;
    font-size: 21px;
    letter-spacing: 1px;
    color: var(--sand);
    line-height: 1;
  }
  .product-name {
    margin-top: 8px;
    font-family: "Playfair Display", Georgia, serif;
    font-weight: 700;
    font-size: 50px;
    line-height: 0.98;
    color: var(--ink-brown);
    letter-spacing: 1px;
  }
  .olive-branch {
    position: absolute;
    top: 520px;
    left: 0;
    width: 283px;
    height: 290px;
    background:
      radial-gradient(ellipse 60% 45% at 60% 50%, var(--leaf-mid) 0%, rgba(169,192,138,0.55) 45%, rgba(223,233,207,0) 80%),
      radial-gradient(ellipse 20% 16% at 58% 52%, var(--olive) 0%, rgba(111,143,58,0) 100%);
  }
  .net-volume {
    position: absolute;
    top: 836px;
    left: 0;
    width: 100%;
    text-align: center;
    font-family: "Oswald", "Arial Narrow", sans-serif;
    font-weight: 500;
    font-size: 11px;
    letter-spacing: 0.6px;
    color: var(--ink-brown);
  }
</style>
</head>
<body>
<main class="canvas">
  <section class="label">
    <h1 class="brand">Harlow<br>Pantry</h1>

    <svg class="gold-wave" viewBox="0 0 283 60" aria-hidden="true">
      <defs>
        <linearGradient id="goldSweep" x1="0" y1="0" x2="1" y2="0">
          <stop offset="0" stop-color="var(--gold-deep)"/>
          <stop offset="0.3" stop-color="var(--gold-light)"/>
          <stop offset="0.6" stop-color="var(--gold-mid)"/>
          <stop offset="1" stop-color="var(--gold-light)"/>
        </linearGradient>
      </defs>
      <path d="M0 32 C 60 40, 110 36, 170 22 C 215 12, 250 8, 283 10 L 283 16 C 250 14, 215 20, 175 30 C 115 44, 60 52, 0 52 Z" fill="url(#goldSweep)"/>
    </svg>

    <div class="product">
      <p class="product-grade">EXTRA VIRGIN</p>
      <h2 class="product-name">OLIVE<br>OIL</h2>
    </div>

    <div class="olive-branch" role="img" aria-label="Watercolour olive branch with green leaves and olives"></div>

    <p class="net-volume">NET WET. 250ML</p>
  </section>
</main>
</body>
</html>
```